BOLD & MINIMALIST DESIGN NEEDED

We want a very bold but minimalistic business card design that is impactful and utilizes both sides of the business card. Our current logo is included for your use.

We want bold fonts and good use of negative space. We don't want the logo to overpower the design.

Target Market(s)

Professionals who are building new commercial buildings.

Industry/Entity Type

Construction

Contact Information for Business Card

Name, Title, email, office phone, cell phone, website

Font styles to use
Serif
Sans Serif

Requirements
Must have
• Bold design!

```html
<!DOCTYPE html>
<html lang="en">
<head>
<meta charset="utf-8">
<title>Ridgeline Design + Build — Business Card</title>
<link href="https://fonts.googleapis.com/css2?family=Montserrat:wght@400;500;700;800&display=swap" rel="stylesheet">
<style>
  :root {
    --stage: #3b3b3b;
    --card: #1d1d1d;
    --card-back: #1a1a1a;
    --lime: #8cc63f;
    --white: #f2f2f2;
    --muted: #d6d6d6;
    --emboss: #2b2b2b;
  }
  * { box-sizing: border-box; margin: 0; padding: 0; }
  html, body {
    width: 1200px; height: 791px; overflow: hidden;
    background: var(--stage);
    font-family: "Montserrat", Arial, sans-serif;
  }
  .stage {
    width: 1200px; height: 791px;
    display: flex; align-items: center; justify-content: center; gap: 40px;
  }
  .card {
    position: relative;
    width: 525px; height: 300px;
    background: var(--card);
    border-bottom: 3px solid var(--lime);
    box-shadow: 0 10px 30px rgba(0,0,0,.35);
  }
  .card--back { background: var(--card-back); }

  /* front */
  .brand {
    position: absolute; left: 40px; top: 70px; width: 230px;
    text-align: center; color: var(--white);
  }
  .brand__mark {
    display: inline-block; width: 14px; height: 14px;
    background: var(--lime); margin-bottom: 8px;
  }
  .brand__name {
    font-weight: 800; font-size: 34px; letter-spacing: 0.5px; line-height: 1;
  }
  .brand__tag {
    font-weight: 800; font-size: 11px; letter-spacing: 4px; margin-top: 6px;
  }
  .divider {
    position: absolute; left: 290px; top: 92px;
    width: 1.5px; height: 62px; background: var(--lime);
  }
  .contact {
    position: absolute; left: 312px; top: 78px;
    list-style: none; color: var(--muted); font-size: 13px; font-weight: 500;
  }
  .contact li { display: flex; align-items: center; gap: 9px; height: 23px; }
  .contact svg { width: 11px; height: 11px; flex: none; }
  .person { position: absolute; left: 40px; bottom: 44px; }
  .person__name {
    color: var(--lime); font-weight: 700; font-size: 24px; letter-spacing: .5px;
  }
  .person__title {
    color: var(--white); font-size: 15px; font-weight: 400; margin-top: 2px; margin-left: 70px;
  }

  /* back */
  .back-brand {
    position: absolute; inset: 0;
    display: flex; align-items: center; justify-content: center;
    color: var(--emboss); font-weight: 800; font-size: 40px; letter-spacing: 1px;
  }
</style>
</head>
<body>
<main class="stage">
  <section class="card card--front">
    <div class="brand">
      <span class="brand__mark"></span>
      <div class="brand__name">RIDGELINE</div>
      <div class="brand__tag">DESIGN + BUILD</div>
    </div>
    <div class="divider"></div>
    <ul class="contact">
      <li><svg viewBox="0 0 12 12"><path fill="#8cc63f" d="M2.5 1l2 2-1 1.3a7 7 0 0 0 4.2 4.2L9 7.5l2 2-1.3 1.5C5.6 11 1 6.4 1 2.3z"/></svg>555-014-2200</li>
      <li><svg viewBox="0 0 12 12"><rect x="3" y="0.8" width="6" height="10.4" rx="1" fill="none" stroke="#8cc63f" stroke-width="1.4"/></svg>555-014-2201</li>
      <li><svg viewBox="0 0 12 12"><rect x="1" y="2.5" width="10" height="7" fill="#8cc63f"/><path d="M1 2.5l5 4 5-4" fill="none" stroke="#1d1d1d" stroke-width="1"/></svg>m.trent@rdb-build.com</li>
      <li><svg viewBox="0 0 12 12"><circle cx="6" cy="6" r="5" fill="#8cc63f"/><path d="M1 6h10M6 1c-2 3-2 7 0 10M6 1c2 3 2 7 0 10" fill="none" stroke="#1d1d1d" stroke-width=".9"/></svg>www.rdb-build.com</li>
    </ul>
    <div class="person">
      <div class="person__name">MARCUS TRENT</div>
      <div class="person__title">President</div>
    </div>
  </section>

  <section class="card card--back">
    <div class="back-brand">RIDGELINE</div>
  </section>
</main>
</body>
</html>
```